Core Values poster for display in office

We want to create a poster that displays our core values which we can print and place in our office and potentially use on our website.

DataHaven is a Cyber Security consultancy that helps its secure its clients from Cyber Criminals.

Our core values are what we live and breath everyday. They are:
- Customer love
- High performing team
- Do the right thing
- An awesome culture
- Innovative

Here they are again with more detail after each:
- Customer love – exchange in abundance
- High performing team – do whatever it takes, no passengers
- Do the right thing – be accountable, maintain our integrity
- An awesome culture – work hard, play hard, collaborate and celebrate success
- Innovative – solving problems with new ideas

We are in the process of rolling out new branding with a load of comic book style super hero's and villains. Attached are some of those images in PDF format for some business card designs for you to review if you want to incorporate, but I will upload these images to this dropbox folder once my designer sends them to me:
https://www.filecrate-share.net/sh/qpwlzrtkc42hbum/XKPq9LmVtR3sDwYuNHaEfG81b?dl=0

I stumbled across another business with the same name as us and saw their values poster, which I liked conceptually.
www.datahaven-example.net
I've attached the image for reference (note this is not our business or values - just saying I like the concept).

Also attached is our logo in EPS format.

We would like the image editing version of the file once complete so we can edit the file in case we change or tweak our values in the near future.

Target Market(s)

This poster is to be displayed internally and maybe on our website in the hiring section

Industry/Entity Type

Office

Colors
0792cd
ffffff
f68e4e
e667a6
fbee3e

Requirements
Must have
• Must have a vibrant, impactful poster that clearly states our core values in a way so that they are understood.
• Must be print ready in high definition (large A2 size poster).
Nice to have
• Integrate our logo

```html
<!DOCTYPE html>
<html lang="en">
<head>
<meta charset="utf-8">
<title>DataHaven — Our Core Values</title>
<link rel="stylesheet" href="https://fonts.googleapis.com/css2?family=Questrial&family=Montserrat:wght@700;800&display=swap">
<style>
  :root {
    --paper: #f2f8fb;
    --brand-blue: #1a93d1;
    --deep-blue: #1d6fa5;
    --ink-blue: #2a6aa3;
    --maroon: #9a2645;
    --maroon-tint: #f1dde3;
    --green: #4d7b26;
    --green-tint: #e2ecd9;
    --navy: #253f8a;
    --navy-tint: #dde2ef;
    --teal: #017075;
    --teal-tint: #d5e9ea;
    --midnight: #032640;
    --midnight-tint: #dbe5ec;
    --purple: #7d3c98;
    --core-teal: #136a8c;
    --forest: #1f6a3a;
    --icon-tint: #b9dcf1;
    --white: #ffffff;
  }
  html, body {
    margin: 0;
    padding: 0;
    width: 849px;
    height: 1200px;
    overflow: hidden;
    background: var(--paper);
  }
  .poster {
    display: block;
    width: 849px;
    height: 1200px;
  }
  .light-type { font-family: "Questrial", "Century Gothic", sans-serif; }
  .heavy-type { font-family: "Montserrat", "Century Gothic", sans-serif; font-weight: 800; }
  .logo-type { font-family: "Montserrat", sans-serif; font-weight: 700; }
  .value-title { fill: var(--white); }
  .value-detail { fill: var(--ink-blue); font-size: 33px; }
  .illustration { fill: var(--icon-tint); opacity: 0.75; }
</style>
</head>
<body>
<svg class="poster" viewBox="0 0 849 1200" xmlns="http://www.w3.org/2000/svg">
  <rect width="849" height="1200" fill="var(--paper)"/>

  <!-- Header clipboard -->
  <g class="header-board">
    <polygon points="0,0 300,0 268,378 0,360" fill="var(--brand-blue)"/>
    <polygon points="0,0 272,0 244,336 0,318" fill="var(--white)"/>
    <text class="heavy-type" x="86" y="90" font-size="62" fill="var(--purple)" transform="rotate(4 86 90)">Our</text>
    <text class="heavy-type" x="30" y="160" font-size="78" fill="var(--core-teal)" transform="rotate(4 30 160)">core</text>
    <text class="heavy-type" x="20" y="222" font-size="64" fill="var(--forest)" transform="rotate(5 20 222)">values</text>
    <polyline points="88,262 112,286 154,250" fill="none" stroke="var(--brand-blue)" stroke-width="9" stroke-linecap="round" stroke-linejoin="round"/>
  </g>

  <!-- Value 1: Customer love -->
  <g class="value value-love">
    <polygon points="324,36 849,36 849,248 384,290" fill="var(--maroon-tint)"/>
    <polygon points="344,0 849,0 849,184 400,232" fill="var(--maroon)"/>
    <rect class="illustration" role="img" aria-label="Heart icon" x="322" y="64" width="166" height="166" rx="70" transform="rotate(-12 405 147)"/>
    <text class="light-type value-title" x="822" y="150" text-anchor="end"><tspan font-size="43">Customer </tspan><tspan font-size="78">love</tspan></text>
    <text class="light-type value-detail" x="820" y="224" text-anchor="end" transform="rotate(-5 820 224)">exchange in abundance</text>
  </g>

  <!-- Value 2: High performing team -->
  <g class="value value-team">
    <polygon points="200,404 849,376 849,506 160,444" fill="var(--green-tint)"/>
    <polygon points="264,294 849,276 849,376 200,404" fill="var(--green)"/>
    <rect class="illustration" role="img" aria-label="Puzzle piece icon" x="690" y="286" width="156" height="150" rx="24" opacity="0.35"/>
    <text class="value-title" x="824" y="384" text-anchor="end"><tspan class="light-type" font-size="42">High performing </tspan><tspan class="heavy-type" font-size="88">team</tspan></text>
    <text class="light-type value-detail" x="226" y="434" transform="rotate(4 226 434)">do whatever it takes, no passengers</text>
  </g>

  <!-- Value 3: Do the right thing -->
  <g class="value value-right">
    <polygon points="0,612 680,632 700,684 0,660" fill="var(--navy-tint)"/>
    <polygon points="0,480 744,492 680,632 0,612" fill="var(--navy)"/>
    <rect class="illustration" role="img" aria-label="Light bulb icon" x="682" y="512" width="142" height="160" rx="64"/>
    <text class="light-type value-title" x="224" y="578"><tspan font-size="42">Do the </tspan><tspan font-size="90">right</tspan><tspan font-size="42"> thing</tspan></text>
    <text class="light-type value-detail" x="30" y="640" transform="rotate(2 30 640)">be accountable, maintain our integrity</text>
  </g>

  <!-- Value 4: An awesome culture -->
  <g class="value value-culture">
    <polygon points="192,804 849,832 849,912 170,890" fill="var(--teal-tint)"/>
    <polygon points="148,708 849,684 849,832 192,804" fill="var(--teal)"/>
    <rect class="illustration" role="img" aria-label="Jumping figure illustration" x="16" y="672" width="184" height="216" rx="40"/>
    <text class="light-type value-title" x="812" y="776" text-anchor="end"><tspan font-size="42">An awesome </tspan><tspan font-size="90">culture</tspan></text>
    <text class="light-type value-detail" x="806" y="852" text-anchor="end" font-size="32" transform="rotate(2 806 852)">work hard, play hard,</text>
    <text class="light-type value-detail" x="816" y="900" text-anchor="end" font-size="32" transform="rotate(2 816 900)">collaborate and celebrate success</text>
  </g>

  <!-- Value 5: Innovative -->
  <g class="value value-innovative">
    <polygon points="0,1032 600,1032 580,1076 0,1084" fill="var(--midnight-tint)"/>
    <polygon points="0,892 584,908 572,1032 0,1032" fill="var(--midnight)"/>
    <rect class="illustration" role="img" aria-label="Rocket illustration" x="420" y="912" width="200" height="200" rx="60" transform="rotate(30 520 1012)"/>
    <text class="light-type value-title" x="112" y="988" font-size="92">Innovative</text>
    <text class="light-type value-detail" x="30" y="1066" transform="rotate(-3 30 1066)">solving problems with new ideas</text>
  </g>

  <!-- Footer with brand name -->
  <g class="footer">
    <rect x="0" y="1124" width="849" height="52" fill="var(--brand-blue)"/>
    <text class="logo-type" x="816" y="1163" text-anchor="end" font-size="36" fill="var(--white)">DataHaven</text>
  </g>
</svg>
</body>
</html>
```